WordPress Website for Pain Relief Clinic

I need a WordPress website designed for my laser pain relief clinic. It needs to be a professional, responsive design with 7 pages: Home, Why Choose Us, Treatable Conditions, Testimonials, FAQ, Franchising, Contact Us. Here is logo: https://files.brivoltcdn.com/media.t-w-e-n.com/sitebuilder/472/CalvexaLogoHighQuality.png

Target Market(s)

people with pain,elderly adults,injuries,soreness

Industry/Entity Type

Clinic

Number of Pages Required

5+ page

Colors
0792cd
85abd2

```html
<!DOCTYPE html>
<html lang="en">
<head>
<meta charset="utf-8">
<title>Calvexa Laser Pain Relief</title>
<link rel="stylesheet" href="https://fonts.googleapis.com/css2?family=Raleway:wght@400;500;600;700&family=Open+Sans:wght@400;600&display=swap">
<style>
:root{
  --brand:#0792cd;
  --brand-soft:#85abd2;
  --brand-deep:#1565b8;
  --nav-top:#3fb0e6;
  --nav-bottom:#0d86c8;
  --ink:#2a2a2a;
  --muted:#6b6b6b;
  --rule:#e2e2e2;
  --footer:#ececec;
  --caption:rgba(38,78,110,.88);
}
*{margin:0;padding:0;box-sizing:border-box}
html,body{width:976px;height:1200px;overflow:hidden;background:#fff}
body{position:relative;font-family:"Open Sans",sans-serif;color:var(--ink)}
.abs{position:absolute}

.site-header{left:0;top:0;width:976px;height:81px;background:#fff}
.logo{left:155px;top:23px;font-family:"Raleway",sans-serif;font-weight:500;font-size:21px;line-height:23px;color:var(--brand)}
.contact-call{right:157px;top:32px;text-align:right;font-family:"Raleway",sans-serif}
.contact-call .label{font-size:13px;color:var(--brand)}
.contact-call .number{display:flex;align-items:center;gap:3px;font-size:19px;color:#333;margin-top:1px}

.main-nav{left:0;top:81px;width:976px;height:37px;background:linear-gradient(var(--nav-top),var(--nav-bottom));display:flex;justify-content:center}
.main-nav a{display:block;padding:0 11px;line-height:37px;font-family:"Raleway",sans-serif;font-weight:500;font-size:12px;color:#fff;text-decoration:none;border-right:1px solid rgba(255,255,255,.18)}
.main-nav a:last-child{border-right:none}

.hero{left:0;top:118px;width:976px;height:362px;background:linear-gradient(110deg,#e7b49a 0%,#f3d4c2 35%,#f8eee8 55%,#eec1a8 75%,#e0a78d 100%)}
.hero-caption{left:155px;top:246px;width:323px;height:127px;background:var(--caption);color:#fff;padding:22px 30px}
.hero-caption h1{font-family:"Raleway",sans-serif;font-weight:600;font-size:25px;line-height:28px}
.hero-caption h2{font-family:"Raleway",sans-serif;font-weight:700;font-size:13.5px;margin-top:3px}
.hero-caption p{font-size:8.5px;line-height:15px;margin-top:6px}
.slider-dots{left:458px;top:457px;display:flex;gap:4px}
.slider-dots span{width:13px;height:13px;border-radius:50%;background:#fff}

.conditions{left:0;top:480px;width:976px;height:136px;background:linear-gradient(#fff 60%,#f0f0f0)}
.condition{width:160px;text-align:center;top:18px}
.condition .icon{width:46px;height:46px;margin:0 auto;border-radius:50%;background:var(--brand)}
.condition h3{font-family:"Raleway",sans-serif;font-weight:500;font-size:16px;color:var(--brand);margin-top:16px}
.condition p{font-size:9.5px;color:var(--muted);margin-top:2px}

.welcome{left:160px;top:644px;width:656px;text-align:center}
.welcome h2{font-family:"Raleway",sans-serif;font-weight:400;font-size:22px;color:#222}
.welcome .lead{font-size:8.6px;color:#444;margin-top:12px}
.welcome .body{font-size:7.6px;line-height:13.6px;color:#555;margin-top:9px}
.btn-book{display:inline-block;margin-top:17px;width:153px;height:31px;line-height:31px;border-radius:2px;background:linear-gradient(#1da2e6,#0a7fd0);color:#fff;font-family:"Raleway",sans-serif;font-weight:500;font-size:12px}
.divider{left:160px;top:808px;width:657px;height:1px;background:var(--rule)}

.feature{width:205px}
.feature .photo{width:205px;height:95px}
.feature h3{font-family:"Raleway",sans-serif;font-weight:500;font-size:16px;color:var(--brand);margin-top:9px}
.feature p{font-size:8px;line-height:14.4px;color:#777;margin-top:4px}
.btn-more{display:inline-block;margin-top:11px;width:78px;height:24px;line-height:24px;text-align:center;background:linear-gradient(#1a6fc4,#0e55a8);color:#fff;font-family:"Raleway",sans-serif;font-weight:600;font-size:9.5px;border-radius:1px}

.site-footer{left:0;top:1094px;width:976px;height:106px;background:var(--footer)}
.footer-links{left:157px;top:33px;font-family:"Raleway",sans-serif;font-size:11.5px;color:#444}
.footer-links span{color:#555;margin:0 4px}
.copyright{left:157px;top:57px;font-size:8px;color:#666}
.social{left:717px;top:30px;display:flex;gap:9px}
.social span{width:17px;height:17px;border-radius:50%}
</style>
</head>
<body>

<header class="site-header abs">
  <div class="logo abs">Calvexa Laser<br>Pain Relief</div>
  <div class="contact-call abs">
    <div class="label">Call Us Now</div>
    <div class="number">
      <svg width="16" height="16" viewBox="0 0 24 24" aria-hidden="true"><path fill="#0792cd" d="M6.6 10.8a15.1 15.1 0 0 0 6.6 6.6l2.2-2.2c.3-.3.7-.4 1-.2 1.1.4 2.3.6 3.6.6.6 0 1 .4 1 1V20c0 .6-.4 1-1 1C10.6 21 3 13.4 3 4c0-.6.4-1 1-1h3.5c.6 0 1 .4 1 1 0 1.3.2 2.5.6 3.6.1.3 0 .7-.2 1z"/></svg>
      555-014-2290
    </div>
  </div>
</header>

<nav class="main-nav abs">
  <a>HOME</a><a>WHY CHOOSE US</a><a>TREATABLE CONDITIONS</a><a>TESTIMONIALS</a><a>FAQ</a><a>FRANCHISING</a><a>CONTACT US</a>
</nav>

<section class="hero abs" role="img" aria-label="Photo of a laser therapy device being applied to a patient's leg">
</section>
<div class="hero-caption abs">
  <h1>LASER PAIN RELIEF</h1>
  <h2>DONEC QUIS SED MAGNA HENDRERIT</h2>
  <p>Class aptent taciti sociosqu ad litora torquent per conubia nostra per inceptos hymenaeos Proin nulla arcu nonummy luctus</p>
</div>
<div class="slider-dots abs"><span></span><span></span><span></span><span></span></div>

<section class="conditions abs">
  <div class="condition abs" style="left:158px"><div class="icon" role="img" aria-label="Back pain icon"></div><h3>Back Pain</h3><p>Mauris vel lacus vitae vestibulum</p></div>
  <div class="condition abs" style="left:326px"><div class="icon" role="img" aria-label="Knee pain icon"></div><h3>Knee pain</h3><p>Mauris vel lacus vitae vestibulum</p></div>
  <div class="condition abs" style="left:492px"><div class="icon" role="img" aria-label="Shoulder pain icon"></div><h3>Shoulder pain</h3><p>Mauris vel lacus vitae vestibulum</p></div>
  <div class="condition abs" style="left:655px"><div class="icon" role="img" aria-label="Muscle pain icon"></div><h3>Muscle pain</h3><p>Mauris vel lacus vitae vestibulum</p></div>
</section>

<section class="welcome abs">
  <h2>Welcome to Our Website Mainpage</h2>
  <p class="lead">Mauris vel lacus vitae felis vestibulum volutpat Etiam est nunc venenatis in tristique eu imperdiet ac nisl</p>
  <p class="body">In iaculis facilisis massa Etiam eu urna Sed porta Suspendisse quam leo molestie sed luctus quis feugiat in pede Fusce tellus Sed metus augue Pellentesque faucibus Ut accumsan ultricies elit Maecenas at justo id velit placerat molestie Donec dictum lectus non odio Cras a ante vitae enim iaculis &nbsp;euismod sit amet egestas placerat es Integer congue augue et malesuada iaculis ipsum dui aliquet felis at cursus magna nisl nec elit Praesent elementum elit at tellus nec ultricies</p>
  <span class="btn-book">Book and Appointment</span>
</section>
<div class="divider abs"></div>

<article class="feature abs" style="left:161px;top:839px">
  <div class="photo" role="img" aria-label="Photo of a laser therapy handpiece" style="background:linear-gradient(120deg,#6e4a3c,#a8786a 55%,#d9c2b8)"></div>
  <h3>Treatable Conditions</h3>
  <p>Vivamus porttitor purus nisi eleifend libero a tempus libero lectus feugiat felis Morbi diam mauris viverra in gravida eu mattis in ante Morbi eget</p>
  <span class="btn-more">READ MORE</span>
</article>
<article class="feature abs" style="left:386px;top:839px">
  <div class="photo" role="img" aria-label="Photo of a laser treatment on a patient's leg" style="background:linear-gradient(120deg,#5a4a44,#c7a18e 50%,#e8d6cc)"></div>
  <h3>Why Choose Us</h3>
  <p>Vivamus porttitor purus nisi eleifend libero a tempus libero lectus feugiat felis Morbi diam mauris viverra in gravida eu mattis in ante Morbi eget</p>
  <span class="btn-more">READ MORE</span>
</article>
<article class="feature abs" style="left:613px;top:839px">
  <div class="photo" role="img" aria-label="Photo of a gloved practitioner treating a shoulder" style="background:linear-gradient(120deg,#e6d9d4,#f4ebe6 50%,#8fc3ea)"></div>
  <h3 style="margin-top:7px">Franchising</h3>
  <p>Vivamus porttitor purus nisi eleifend libero a tempus libero lectus feugiat felis Morbi diam mauris viverra in gravida eu mattis in ante Morbi eget</p>
  <span class="btn-more">READ MORE</span>
</article>

<footer class="site-footer abs">
  <div class="footer-links abs">Home<span>|</span>Why Choose Us<span>|</span>Treatable Conditions<span>|</span>Testimonials<span>|</span>FAQ<span>|</span>Franchising<span>|</span>Contact Us</div>
  <div class="copyright abs">© 2015 Company Name &nbsp;All right reserved &nbsp;Term of Use</div>
  <div class="social abs">
    <span style="background:#2aa3e0"></span><span style="background:#1e4f8f"></span><span style="background:#1b64a8"></span><span style="background:#d9412b"></span>
  </div>
</footer>

</body>
</html>
```